pop up booking component and calendar re-design

we have a calander view where a parent cant reserve a day
you can click on please redesign the calander / voucher and pop up.

the dropdowns in pop up can be buttons
the dots on the calander indicate if there is space or not

when booking a day you can select a voucher

we used KIVO as inspiration, you are welcome to look at it as well.. screenshots attached

please ask questions if you have any

```html
<!DOCTYPE html>
<html lang="en">
<head>
<meta charset="utf-8">
<title>Pop-up booking component and Calendar Re-Design</title>
<link href="https://fonts.googleapis.com/css2?family=Poppins:wght@600&family=Roboto:wght@400;500;700&display=swap" rel="stylesheet">
<style>
:root{
  --page:#ffffff;
  --blob:#f1f4fd;
  --panel:#f9f9fa;
  --card:#ffffff;
  --line:#ececec;
  --muted:#a9a9a9;
  --text:#3b3b3b;
  --accent:#1b6fe8;
  --brand-dot:#2563d9;
  --ring:#a9ecd2;
  --blue-bg:#d7eefb;--blue-tx:#1d73bd;--blue-bd:#2196f3;
  --green-bg:#ddf5d6;--green-tx:#2b9528;--green-bd:#4caf50;
  --pink-bg:#fde2ea;--pink-tx:#df2a5e;--pink-bd:#e53d6c;
  --orange-bg:#fdebd2;--orange-tx:#dd7410;--orange-bd:#f39c33;
  --purple-bg:#f3e2f7;--purple-tx:#9a3daf;--purple-bd:#b04ac6;
  --yellow-bg:#fdf3d6;--yellow-tx:#a98400;--yellow-bd:#f2c318;
  --brown-bg:#f3e7df;--brown-tx:#87563a;--brown-bd:#9b6a4c;
}
*{box-sizing:border-box;margin:0;padding:0}
html,body{width:1200px;height:2203px;overflow:hidden}
body{background:var(--page);font-family:'Roboto',sans-serif;color:var(--text);position:relative}
.backdrop{position:absolute;inset:0}
.page-title{position:absolute;left:92px;top:940px;transform:rotate(-90deg);transform-origin:0 0;font-family:'Poppins',sans-serif;font-weight:600;font-size:29px;white-space:nowrap;color:#1a1a1a;letter-spacing:-.2px}
.panel{position:absolute;background:var(--panel);box-shadow:0 20px 50px rgba(90,110,200,.12)}
.panel-top{left:187px;top:171px;width:877px;height:913px}
.panel-bottom{left:188px;top:1146px;width:877px;height:913px}
.card{position:absolute;background:var(--card);box-shadow:0 1px 4px rgba(0,0,0,.05)}
.cal-header{position:absolute;left:0;top:0;right:0;height:55px;border-bottom:1px solid var(--line)}
.nav-arrows{position:absolute;left:15px;top:16px;width:50px;height:24px;border:1px solid var(--line);display:flex}
.nav-arrows span{flex:1;display:flex;align-items:center;justify-content:center}
.nav-arrows span+span{border-left:1px solid var(--line)}
.btn-today{position:absolute;left:77px;top:16px;width:47px;height:24px;border:1px solid var(--line);font-size:5px;color:#999;display:flex;align-items:center;justify-content:center;letter-spacing:.5px}
.cal-title{position:absolute;left:0;right:0;top:18px;text-align:center;font-size:12.5px;color:#333}
.view-switch{position:absolute;left:531px;top:16px;height:24px;display:flex;border:1px solid var(--line)}
.view-switch span{font-size:5px;color:#999;letter-spacing:.5px;display:flex;align-items:center;justify-content:center}
.view-switch .is-active{background:#f4f4f4}
.v-day{width:35px}.v-week{width:47px;border-left:1px solid var(--line)}.v-month{width:48px;border-left:1px solid var(--line)}
/* month */
.month-grid{position:absolute;left:0;top:55px;width:677px;display:grid;grid-template-columns:repeat(7,1fr);grid-template-rows:55px repeat(5,73px)}
.weekday{font-size:7px;font-weight:700;color:#aaa;letter-spacing:.8px;display:flex;align-items:center;justify-content:center;border-right:1px solid var(--line);border-bottom:1px solid var(--line)}
.day-cell{position:relative;border-right:1px solid var(--line);border-bottom:1px solid var(--line)}
.weekday:nth-child(7n),.day-cell:nth-child(7n){border-right:none}
.day-cell:nth-last-child(-n+7){border-bottom:none}
.day-num{position:absolute;right:6px;top:6px;font-size:8px;color:var(--muted)}
.holiday{position:absolute;left:0;right:0;top:0;height:18px;background:#f5f5f5}
.holiday-label{position:absolute;left:6px;top:6px;font-size:7px;color:#555}
.day-num.today{background:#e53935;color:#fff;font-weight:700;font-size:7px;padding:1px 3px;border-radius:2px;top:5px}
.pill{position:absolute;left:4px;right:4px;height:15px;font-size:7px;font-weight:500;line-height:15px;padding-left:6px;white-space:nowrap;overflow:hidden}
.p1{top:19px}.p2{top:41px}
.blue{background:var(--blue-bg);color:var(--blue-tx);border-color:var(--blue-bd)}
.green{background:var(--green-bg);color:var(--green-tx);border-color:var(--green-bd)}
.pink{background:var(--pink-bg);color:var(--pink-tx);border-color:var(--pink-bd)}
.orange{background:var(--orange-bg);color:var(--orange-tx);border-color:var(--orange-bd)}
.purple{background:var(--purple-bg);color:var(--purple-tx);border-color:var(--purple-bd)}
.yellow{background:var(--yellow-bg);color:var(--yellow-tx);border-color:var(--yellow-bd)}
.brown{background:var(--brown-bg);color:var(--brown-tx);border-color:var(--brown-bd)}
/* week */
.week-head{position:absolute;left:0;top:55px;right:0;height:53px;border-bottom:1px solid var(--line)}
.week-head span{position:absolute;top:0;width:91px;height:53px;display:flex;align-items:center;justify-content:center;font-size:7px;font-weight:700;letter-spacing:.8px;color:#aaa;border-left:1px solid var(--line)}
.time-body{position:absolute;left:0;right:0}
.hline{position:absolute;left:0;right:0;height:1px;background:var(--line)}
.vline{position:absolute;top:0;bottom:0;width:1px;background:var(--line)}
.tlabel{position:absolute;font-size:7px;color:#999;width:39px;text-align:center}
.evt{position:absolute;border-left:2px solid;font-size:7px;font-weight:500;padding:4px 5px;line-height:1.45;overflow:hidden;white-space:nowrap}
.evt.wrap{white-space:normal}
.allday{position:absolute;background:#f5f5f5;font-size:7px;color:#555;padding:5px 6px;height:19px}
.evt .tm{margin-right:8px}
.evt.row{padding:8px 12px}
/* mini calendar */
.mini{position:absolute;font-size:7px;color:#555;text-align:center;width:22px}
.mini.hd{font-weight:500;color:#444}
.mini.out{color:#ccc}
.mini.sel{background:#eee;border-radius:50%;height:14px;line-height:14px;top:auto}
.detail-title{position:absolute;left:463px;top:257px;font-size:9.5px;line-height:17px;color:#333;width:200px}
.detail-meta{position:absolute;left:463px;font-size:7.5px;color:#999}
/* forms */
.form-title{position:absolute;top:20px;font-size:10.5px;color:#333}
.close{position:absolute;top:22px}
.form-line{position:absolute;left:0;right:0;top:53px;height:1px;background:var(--line)}
.field{position:absolute;height:29px;border:1px solid var(--line);font-size:7px;color:#444;padding-left:12px;display:flex;align-items:center}
.field.select::after{content:"";position:absolute;right:11px;top:11px;width:4px;height:4px;border-right:1px solid #aaa;border-bottom:1px solid #aaa;transform:rotate(45deg)}
.flabel{position:absolute;font-size:7px;color:#555}
.btn-primary{position:absolute;left:19px;top:262px;width:85px;height:30px;background:var(--accent);color:#fff;font-size:7px;font-weight:700;letter-spacing:.8px;display:flex;align-items:center;justify-content:center}
</style>
</head>
<body>
<svg class="backdrop" width="1200" height="2203" viewBox="0 0 1200 2203" aria-hidden="true">
  <path d="M1064 260 C1130 262 1170 270 1200 276 L1200 1000 C1150 1080 1080 1130 990 1150 L760 1150 C720 1110 690 1090 670 1084 Z" fill="var(--blob)"/>
  <path d="M0 1150 C40 1150 60 1240 80 1330 C110 1480 150 1560 188 1580 L188 1690 C120 1680 60 1670 0 1686 Z" fill="var(--blob)"/>
  <path d="M0 1800 C300 1900 600 2000 1065 2040 L1065 2059 L1065 2203 L0 2203 Z" fill="var(--blob)"/>
  <path d="M1065 2020 C1160 1990 1200 1960 1200 1960 L1200 2203 L890 2203 C900 2130 940 2060 1065 2020 Z" fill="#eef2fc"/>
  <path d="M0 760 C40 660 100 610 160 605" stroke="#eef0f6" fill="none" stroke-dasharray="3 3"/>
  <path d="M0 1760 C50 1640 110 1590 188 1580" stroke="#eef0f6" fill="none" stroke-dasharray="3 3"/>
  <circle cx="19" cy="212" r="40" fill="var(--brand-dot)"/>
  <circle cx="219" cy="126" r="16" fill="none" stroke="var(--ring)" stroke-width="5"/>
  <circle cx="537" cy="0" r="28" fill="none" stroke="#f0f0f4"/>
  <circle cx="485" cy="23" r="4" fill="#c9f2df"/>
  <path d="M409 16l5 5M414 16l-5 5M522 62l4 4M526 62l-4 4" stroke="#c9d4f3" stroke-width="1"/>
  <line x1="187" y1="1025" x2="187" y2="1084" stroke="#2f6fe0"/>
  <line x1="188" y1="2000" x2="188" y2="2059" stroke="#2f6fe0"/>
</svg>

<h1 class="page-title">Pop-up booking component and Calendar Re-Design</h1>

<!-- Top panel -->
<section class="panel panel-top">
  <!-- Month view -->
  <div class="card" style="left:100px;top:55px;width:677px;height:475px">
    <div class="cal-header">
      <div class="nav-arrows"><span><svg width="12" height="8" viewBox="0 0 12 8"><path d="M11 4H1M4 1L1 4l3 3" fill="none" stroke="#aaa"/></svg></span><span><svg width="12" height="8" viewBox="0 0 12 8"><path d="M1 4h10M8 1l3 3-3 3" fill="none" stroke="#aaa"/></svg></span></div>
      <div class="btn-today">TODAY</div>
      <div class="cal-title">September 2016</div>
      <div class="view-switch"><span class="v-day">DAY</span><span class="v-week">WEEK</span><span class="v-month is-active">MONTH</span></div>
    </div>
    <div class="month-grid">
      <div class="weekday">SUNDAY</div><div class="weekday">MONDAY</div><div class="weekday">TUESDAY</div><div class="weekday">WEDNESDAY</div><div class="weekday">THURSDAY</div><div class="weekday">FRIDAY</div><div class="weekday">SATURDAY</div>

      <div class="day-cell"><span class="day-num">28</span></div>
      <div class="day-cell"><div class="holiday"></div><span class="holiday-label">New Year's Day</span><span class="day-num" style="color:#333;font-weight:500">29</span><div class="pill p1 purple">The amazing hubble...</div><div class="pill p2 orange">Branding do you know</div></div>
      <div class="day-cell"><span class="day-num">30</span></div>
      <div class="day-cell"><span class="day-num">31</span><div class="pill p1 green">Universe through a ...</div></div>
      <div class="day-cell"><span class="day-num">1 September</span></div>
      <div class="day-cell"><span class="day-num">2</span></div>
      <div class="day-cell"><span class="day-num">3</span></div>

      <div class="day-cell"><span class="day-num">4</span><div class="pill p1 orange">Easy steps clearer skin</div></div>
      <div class="day-cell"><span class="day-num">5</span></div>
      <div class="day-cell"><span class="day-num">6</span></div>
      <div class="day-cell"><span class="day-num">7</span><div class="pill p1 pink">Universe through a c...</div></div>
      <div class="day-cell"><span class="day-num">8</span><div class="pill p1 orange">Top 3 Reasons Why...</div></div>
      <div class="day-cell"><span class="day-num today">9</span></div>
      <div class="day-cell"><span class="day-num">10</span></div>

      <div class="day-cell"><span class="day-num">11</span></div>
      <div class="day-cell"><span class="day-num">12</span></div>
      <div class="day-cell"><span class="day-num">13</span><div class="pill p1 purple">The amazing hubble...</div></div>
      <div class="day-cell"><span class="day-num">14</span></div>
      <div class="day-cell"><span class="day-num">15</span></div>
      <div class="day-cell"><span class="day-num">16</span><div class="pill p1 purple">The amazing hubble...</div></div>
      <div class="day-cell"><span class="day-num">17</span></div>

      <div class="day-cell"><span class="day-num">18</span></div>
      <div class="day-cell"><span class="day-num">19</span><div class="pill p1 pink">The amazing hubble...</div></div>
      <div class="day-cell"><span class="day-num">20</span></div>
      <div class="day-cell"><div class="holiday"></div><span class="holiday-label">New Year's Day</span><span class="day-num">21</span><div class="pill p1 green">Cooking For One</div></div>
      <div class="day-cell"><span class="day-num">22</span></div>
      <div class="day-cell"><span class="day-num">23</span></div>
      <div class="day-cell"><span class="day-num">24</span></div>

      <div class="day-cell"><span class="day-num">25</span></div>
      <div class="day-cell"><span class="day-num">26</span></div>
      <div class="day-cell"><span class="day-num">27</span><div class="pill p1 purple">The universe through...</div></div>
      <div class="day-cell"><span class="day-num">28</span></div>
      <div class="day-cell"><span class="day-num">29</span></div>
      <div class="day-cell"><div class="holiday"></div><span class="holiday-label">Columbus Day</span><span class="day-num">30</span></div>
      <div class="day-cell"><span class="day-num">31</span></div>
    </div>
  </div>

  <!-- Week view -->
  <div class="card" style="left:100px;top:549px;width:677px;height:310px">
    <div class="cal-header">
      <div class="nav-arrows"><span><svg width="12" height="8" viewBox="0 0 12 8"><path d="M11 4H1M4 1L1 4l3 3" fill="none" stroke="#aaa"/></svg></span><span><svg width="12" height="8" viewBox="0 0 12 8"><path d="M1 4h10M8 1l3 3-3 3" fill="none" stroke="#aaa"/></svg></span></div>
      <div class="btn-today">TODAY</div>
      <div class="cal-title">September 2016</div>
      <div class="view-switch"><span class="v-day">DAY</span><span class="v-week is-active">WEEK</span><span class="v-month">MONTH</span></div>
    </div>
    <div class="week-head">
      <span style="left:39px">SUNDAY, &nbsp;2</span><span style="left:130px">MONDAY, &nbsp;3</span><span style="left:221px">TUESDAY, &nbsp;4</span><span style="left:312px">WEDNESDAY, &nbsp;5</span><span style="left:403px">THURSDAY, &nbsp;6</span><span style="left:494px">FRIDAY, &nbsp;7</span><span style="left:585px">SATURDAY, &nbsp;8</span>
    </div>
    <div class="time-body" style="top:108px;height:202px">
      <div class="vline" style="left:39px"></div><div class="vline" style="left:130px"></div><div class="vline" style="left:221px"></div><div class="vline" style="left:312px"></div><div class="vline" style="left:403px"></div><div class="vline" style="left:494px"></div><div class="vline" style="left:585px"></div>
      <div class="hline" style="top:19px"></div><div class="hline" style="top:56px"></div><div class="hline" style="top:92px"></div><div class="hline" style="top:129px"></div><div class="hline" style="top:165px"></div>
      <span class="tlabel" style="top:6px;left:-8px">day</span>
      <span class="tlabel" style="top:52px;left:-8px">1:00</span>
      <span class="tlabel" style="top:88px;left:-8px">2:00</span>
      <span class="tlabel" style="top:125px;left:-8px">3:00</span>
      <span class="tlabel" style="top:161px;left:-8px">4:00</span>
      <div class="allday" style="left:131px;top:0;width:90px">New Year's Day</div>
      <div class="evt pink" style="left:131px;top:19px;width:90px;height:19px">Universe through a c...</div>
      <div class="evt orange" style="left:131px;top:38px;width:90px;height:18px">The basics of buying...</div>
      <div class="evt purple wrap" style="left:131px;top:129px;width:90px;height:55px">Dealing With Technical Support 10 Useful Tips</div>
      <div class="evt blue wrap" style="left:222px;top:56px;width:90px;height:36px">Cooking On A Harlan Brisket Grill</div>
      <div class="evt green" style="left:313px;top:129px;width:90px;height:18px">Universe through a c...</div>
      <div class="evt yellow" style="left:404px;top:92px;width:90px;height:18px">Do a sporting stag do ...</div>
      <div class="evt orange wrap" style="left:495px;top:56px;width:90px;height:73px">What if they let You Run The Hubble</div>
      <div class="evt brown" style="left:495px;top:165px;width:90px;height:19px">Universe through a c...</div>
    </div>
  </div>
</section>

<!-- Bottom panel -->
<section class="panel panel-bottom">
  <!-- Day view with mini calendar -->
  <div class="card" style="left:101px;top:54px;width:675px;height:476px">
    <div class="cal-header">
      <div class="nav-arrows"><span><svg width="12" height="8" viewBox="0 0 12 8"><path d="M11 4H1M4 1L1 4l3 3" fill="none" stroke="#aaa"/></svg></span><span><svg width="12" height="8" viewBox="0 0 12 8"><path d="M1 4h10M8 1l3 3-3 3" fill="none" stroke="#aaa"/></svg></span></div>
      <div class="btn-today">TODAY</div>
      <div class="cal-title">September 2016</div>
      <div class="view-switch"><span class="v-day">DAY</span><span class="v-week">WEEK</span><span class="v-month">MONTH</span></div>
    </div>
    <div class="time-body" style="top:55px;height:421px;right:230px">
      <div class="vline" style="left:39px"></div>
      <div class="vline" style="left:444px"></div>
      <div class="hline" style="top:19px"></div><div class="hline" style="top:55px"></div><div class="hline" style="top:92px"></div><div class="hline" style="top:128px"></div><div class="hline" style="top:165px"></div><div class="hline" style="top:201px"></div><div class="hline" style="top:238px"></div><div class="hline" style="top:274px"></div><div class="hline" style="top:311px"></div><div class="hline" style="top:347px"></div><div class="hline" style="top:384px"></div>
      <span class="tlabel" style="top:6px">day</span>
      <span class="tlabel" style="top:51px">1:00</span>
      <span class="tlabel" style="top:88px">2:00</span>
      <span class="tlabel" style="top:124px">3:00</span>
      <span class="tlabel" style="top:161px">4:00</span>
      <span class="tlabel" style="top:197px">5:00</span>
      <span class="tlabel" style="top:234px">6:00</span>
      <span class="tlabel" style="top:270px">8:00</span>
      <span class="tlabel" style="top:307px">9:00</span>
      <span class="tlabel" style="top:343px">10:00</span>
      <span class="tlabel" style="top:380px">11:00</span>
      <div class="allday" style="left:40px;top:0;width:404px;background:#fafafa">New Year's Day</div>
      <div class="evt row blue" style="left:40px;top:19px;width:404px;height:36px"><span class="tm">12:00</span>Cooking On A Harlan Brisket Grill</div>
      <div class="evt row green" style="left:40px;top:55px;width:404px;height:37px"><span class="tm">12:00</span>Cooking On A Harlan Brisket Grill</div>
      <div class="evt row pink" style="left:40px;top:92px;width:210px;height:73px"><span class="tm">02:00</span>Dude You Re Getting A Telescope</div>
      <div class="evt row orange" style="left:250px;top:92px;width:194px;height:36px"><span class="tm">2:00</span>Cooking On A Harlan Brisket Grill</div>
      <div class="evt row purple" style="left:40px;top:201px;width:404px;height:37px"><span class="tm">5:00</span>Nortwell patch management for home users</div>
      <div class="evt row orange" style="left:40px;top:274px;width:404px;height:37px"><span class="tm">8:00</span>Tourism is back in full swing in cancun mexico</div>
      <div class="evt row green" style="left:40px;top:311px;width:404px;height:36px"><span class="tm">9:00</span>Comment on the importance of human life</div>
    </div>

    <!-- mini month -->
    <span class="mini hd" style="left:464px;top:74px">MO</span><span class="mini hd" style="left:494px;top:74px">TU</span><span class="mini hd" style="left:522px;top:74px">WE</span><span class="mini hd" style="left:550px;top:74px">TH</span><span class="mini hd" style="left:580px;top:74px">FR</span><span class="mini hd" style="left:609px;top:74px">SA</span><span class="mini hd" style="left:635px;top:74px">SU</span>
    <span class="mini out" style="left:464px;top:101px">28</span><span class="mini out" style="left:494px;top:101px">29</span><span class="mini out" style="left:522px;top:101px">30</span><span class="mini out" style="left:550px;top:101px">31</span><span class="mini" style="left:580px;top:101px">1</span><span class="mini" style="left:609px;top:101px">2</span><span class="mini" style="left:635px;top:101px">3</span>
    <span class="mini" style="left:464px;top:128px">4</span><span class="mini" style="left:494px;top:128px">5</span><span class="mini" style="left:522px;top:128px">6</span><span class="mini" style="left:550px;top:128px">7</span><span class="mini sel" style="left:584px;top:124px;width:14px">8</span><span class="mini" style="left:609px;top:128px">9</span><span class="mini" style="left:635px;top:128px">10</span>
    <span class="mini" style="left:464px;top:155px">11</span><span class="mini" style="left:494px;top:155px">12</span><span class="mini" style="left:522px;top:155px">13</span><span class="mini" style="left:550px;top:155px">14</span><span class="mini" style="left:580px;top:155px">15</span><span class="mini" style="left:609px;top:155px">16</span><span class="mini" style="left:635px;top:155px">17</span>
    <span class="mini" style="left:464px;top:182px">18</span><span class="mini" style="left:494px;top:182px">19</span><span class="mini" style="left:522px;top:182px">20</span><span class="mini" style="left:550px;top:182px">21</span><span class="mini" style="left:580px;top:182px">22</span><span class="mini" style="left:609px;top:182px">23</span><span class="mini" style="left:635px;top:182px">24</span>
    <span class="mini" style="left:464px;top:209px">25</span><span class="mini" style="left:494px;top:209px">26</span><span class="mini" style="left:522px;top:209px">27</span><span class="mini" style="left:550px;top:209px">28</span><span class="mini" style="left:580px;top:209px">29</span><span class="mini" style="left:609px;top:209px">30</span><span class="mini" style="left:635px;top:209px">31</span>
    <div class="hline" style="top:238px;left:445px"></div>
    <p class="detail-title">Nortwell patch management for home users</p>
    <p class="detail-meta" style="top:316px">Thursday, 9 &nbsp;&nbsp;September</p>
    <p class="detail-meta" style="top:334px">5:00 AM – 6:00 AM</p>
  </div>

  <!-- Create events, full -->
  <div class="card" style="left:101px;top:549px;width:386px;height:309px">
    <h2 class="form-title" style="left:19px;font-weight:400">Create events</h2>
    <svg class="close" style="left:355px" width="9" height="9" viewBox="0 0 9 9"><path d="M1 1l7 7M8 1L1 8" stroke="#bbb"/></svg>
    <div class="form-line"></div>
    <div class="field" style="left:19px;top:73px;width:167px">New Event</div>
    <div class="field" style="left:201px;top:73px;width:167px">Location</div>
    <span class="flabel" style="left:22px;top:123px">Start Time</span>
    <span class="flabel" style="left:204px;top:123px">Ends Time</span>
    <div class="field select" style="left:19px;top:143px;width:75px">04-09-2016</div>
    <div class="field select" style="left:110px;top:143px;width:76px">05:25 PM</div>
    <div class="field select" style="left:201px;top:143px;width:75px">04-09-2016</div>
    <div class="field select" style="left:292px;top:143px;width:76px">05:25 PM</div>
    <span class="flabel" style="left:22px;top:194px">Reapet</span>
    <span class="flabel" style="left:113px;top:194px">Travel Time</span>
    <span class="flabel" style="left:204px;top:194px">Alert</span>
    <span class="flabel" style="left:295px;top:194px">All-day</span>
    <div class="field select" style="left:19px;top:213px;width:75px">Never</div>
    <div class="field select" style="left:110px;top:213px;width:76px">None</div>
    <div class="field select" style="left:201px;top:213px;width:75px">None</div>
    <div class="field select" style="left:292px;top:213px;width:76px">No</div>
    <div class="btn-primary">ADD EVENTS</div>
  </div>

  <!-- Create events, compact -->
  <div class="card" style="left:506px;top:549px;width:270px;height:309px">
    <h2 class="form-title" style="left:18px;font-weight:400">Create events</h2>
    <svg class="close" style="left:239px" width="9" height="9" viewBox="0 0 9 9"><path d="M1 1l7 7M8 1L1 8" stroke="#bbb"/></svg>
    <div class="form-line"></div>
    <div class="field" style="left:18px;top:73px;width:234px">New Event</div>
    <div class="field" style="left:18px;top:119px;width:234px">Location</div>
    <span class="flabel" style="left:30px;top:176px">Starts time:</span>
    <div class="field select" style="left:82px;top:165px;width:79px">22 Apr 2016</div>
    <div class="field select" style="left:176px;top:165px;width:76px">05:25 PM</div>
    <span class="flabel" style="left:30px;top:222px">Ends time:</span>
    <div class="field select" style="left:82px;top:210px;width:79px">22 Apr 2016</div>
    <div class="field select" style="left:176px;top:210px;width:76px">05:25 PM</div>
    <div class="btn-primary" style="left:18px">ADD EVENT</div>
  </div>
</section>
</body>
</html>
```